Coastal Bright Sweep Business Card

We are a cleaning and waste management company with the slogan "making waste to landfill a thing of the past". We would like a re-design of our current business card. On the front we want to continue to use our logo as the focus point. On the back, we want the whole thing re-done to be less busy. We want the staff member’s name, the job title, mobile number, email and website. We do not want the address on the card. We still want the green, black and blue colours used, but a new font for the information on the back. Please do not change the logo design at all. We are also thinking about using icons to replace the text ‘mobile, email, website’. The “events + commercial” banner needs to be incorporated somewhere and needs to read “events + commercial + waste”. Another important point for consideration is that we are very concerned about being environmentally sustainable and will be printing on recycled paper. All designs should be made to compliment this in regards to boldness and colouring. Please find attached our logo, our colour chart and an image of our current business card.

```html
<!DOCTYPE html>
<html lang="en">
<head>
<meta charset="utf-8">
<title>Coastal Bright Sweep Business Card</title>
<link rel="stylesheet" href="https://fonts.googleapis.com/css2?family=Roboto+Condensed:wght@400;700&display=swap">
<style>
  :root {
    --navy: #123f70;
    --green: #7dc242;
    --sky: #29abe2;
    --white: #ffffff;
    --backdrop: #e8e3da;
    --shadow: rgba(0, 0, 0, 0.28);
  }
  * { margin: 0; padding: 0; box-sizing: border-box; }
  html, body {
    width: 1200px;
    height: 930px;
    overflow: hidden;
    background: var(--backdrop);
    font-family: "Roboto Condensed", Arial, sans-serif;
  }
  .canvas { position: relative; width: 1200px; height: 930px; }
  .card {
    position: absolute;
    left: 278px;
    width: 644px;
    height: 368px;
    border-radius: 22px;
    background: var(--navy);
    overflow: hidden;
    box-shadow: 0 6px 14px var(--shadow);
  }
  .card-front { top: 76px; }
  .card-back { top: 486px; }

  .staff-name {
    position: absolute; left: 32px; top: 36px;
    color: var(--white); font-weight: 700; font-size: 30px; letter-spacing: 0.2px;
  }
  .staff-role {
    position: absolute; left: 32px; top: 68px;
    color: var(--green); font-size: 16px;
  }
  .contact-list {
    position: absolute; left: 32px; top: 272px; list-style: none;
  }
  .contact-list li {
    display: flex; align-items: center; gap: 9px;
    height: 20px; color: var(--white); font-size: 15.5px;
  }
  .contact-list svg { width: 10px; height: 10px; flex: none; }

  .brand-seal { position: absolute; left: 0; top: 0; }
  .seal-name {
    font-family: "Roboto Condensed", Arial, sans-serif;
    font-weight: 700; font-size: 40px; fill: var(--navy);
  }
  .seal-line { font-family: "Roboto Condensed", Arial, sans-serif; font-size: 29px; letter-spacing: 1px; }
  .seal-line.green { fill: var(--green); }
  .seal-line.navy { fill: var(--navy); }
  .slogan {
    font-family: "Roboto Condensed", Arial, sans-serif;
    font-size: 18px; fill: var(--navy); letter-spacing: 1px;
  }

  .back-brand {
    position: absolute; inset: 0;
    display: flex; flex-direction: column; align-items: center; justify-content: center;
    color: var(--white); font-weight: 700; font-size: 62px; line-height: 1.05; text-align: center;
  }
</style>
</head>
<body>
<main class="canvas">

  <section class="card card-front" aria-label="Business card front">
    <svg class="brand-seal" width="644" height="368" viewBox="0 0 644 368">
      <defs>
        <path id="slogan-arc" d="M 292 184 A 168 168 0 0 0 628 184" />
      </defs>
      <circle cx="460" cy="184" r="184" fill="#ffffff" />
      <text class="seal-name" x="460" y="110" text-anchor="middle">Coastal Bright</text>
      <text class="seal-name" x="460" y="152" text-anchor="middle">Sweep</text>
      <text class="seal-line green" x="460" y="236" text-anchor="middle">Events</text>
      <text class="seal-line navy" x="460" y="271" text-anchor="middle">commercial</text>
      <text class="seal-line green" x="460" y="306" text-anchor="middle">waste</text>
      <text class="slogan">
        <textPath href="#slogan-arc" startOffset="0" textLength="520" lengthAdjust="spacing">MAKING WASTE TO LANDFILL A THING OF THE PAST</textPath>
      </text>
    </svg>

    <h1 class="staff-name">MORGAN ELLERY</h1>
    <p class="staff-role">Client Manager</p>

    <ul class="contact-list">
      <li>
        <svg viewBox="0 0 10 10" aria-hidden="true"><path d="M2 1 L3.6 1 L4.2 3 L3.2 3.8 Q4 5.8 6.2 6.8 L7 5.8 L9 6.4 L9 8 Q8.6 9 7.4 9 Q1 8 1 2.4 Q1 1 2 1 Z" fill="#29abe2"/></svg>
        <span>0400 555 218</span>
      </li>
      <li>
        <svg viewBox="0 0 10 10" aria-hidden="true"><rect x="0.8" y="2" width="8.4" height="6" fill="none" stroke="#29abe2" stroke-width="1"/><path d="M0.8 2 L5 5.4 L9.2 2" fill="none" stroke="#29abe2" stroke-width="1"/></svg>
        <span>mellery@coastalbrightsweep.com.au</span>
      </li>
      <li>
        <svg viewBox="0 0 10 10" aria-hidden="true"><circle cx="5" cy="5" r="4" fill="none" stroke="#29abe2" stroke-width="1"/><ellipse cx="5" cy="5" rx="1.8" ry="4" fill="none" stroke="#29abe2" stroke-width="0.8"/><path d="M1 5 H9" stroke="#29abe2" stroke-width="0.8"/></svg>
        <span>www.coastalbrightsweep.com.au</span>
      </li>
    </ul>
  </section>

  <section class="card card-back" aria-label="Business card back">
    <div class="back-brand">
      <span>Coastal Bright</span>
      <span>Sweep</span>
    </div>
  </section>

</main>
</body>
</html>
```